business cards

we want our logos on the back
the information on it are on the design I've uploaded
come up with whatever you think is best, we want something professional, sophisticated and sleek.

```html
<!DOCTYPE html>
<html lang="en">
<head>
<meta charset="utf-8">
<title>Verta Health and Performance – Business Cards</title>
<link href="https://fonts.googleapis.com/css2?family=Montserrat:wght@300;400;500&display=swap" rel="stylesheet">
<style>
  :root {
    --stage: #d9dce1;
    --stage-edge: #b9bec6;
    --card-light: #f4f5f6;
    --card-dark: #262626;
    --ink: #1f1f1f;
    --rule: #2a2a2a;
    --paper-text: #ffffff;
    --accent: #3fae49;
  }
  * { box-sizing: border-box; margin: 0; padding: 0; }
  html, body { width: 1200px; height: 675px; overflow: hidden; }
  body {
    background: radial-gradient(ellipse at 40% 55%, #eceef0 0%, var(--stage) 55%, var(--stage-edge) 100%);
    font-family: "Montserrat", sans-serif;
    position: relative;
  }
  .card {
    position: absolute;
    top: 189px;
    width: 520px;
    height: 297px;
    border-radius: 3px;
    box-shadow: 0 18px 40px rgba(0,0,0,.22), 0 2px 6px rgba(0,0,0,.15);
    overflow: hidden;
  }
  /* Back: appointment card */
  .card--back { left: 60px; background: var(--card-light); color: var(--ink); }
  .appointment__title {
    position: absolute; top: 40px; left: 0; right: 0;
    text-align: center; font-size: 19px; font-weight: 400; letter-spacing: .3px;
  }
  .appointment__lines { position: absolute; top: 92px; left: 60px; right: 60px; }
  .appointment__line { height: 1px; background: var(--rule); margin-bottom: 38px; }
  .social { position: absolute; bottom: 34px; left: 0; right: 0; display: flex; justify-content: center; gap: 8px; }
  .social__dot { width: 18px; height: 18px; border-radius: 50%; background: var(--accent); }

  /* Front: brand and contacts */
  .card--front { left: 620px; background: var(--card-dark); color: var(--paper-text); }
  .brand { position: absolute; top: 52px; left: 40px; }
  .brand__name { display: flex; align-items: center; gap: 14px; font-size: 46px; font-weight: 300; letter-spacing: 22px; line-height: 1; }
  .brand__mark { width: 12px; height: 12px; border-radius: 50%; background: var(--accent); }
  .brand__tagline { margin-top: 10px; font-size: 9px; font-weight: 400; letter-spacing: 6.5px; text-transform: uppercase; }
  .contacts { position: absolute; left: 40px; bottom: 34px; list-style: none; font-size: 13.5px; font-weight: 400; letter-spacing: .3px; }
  .contacts__item { display: flex; align-items: center; gap: 9px; line-height: 20px; }
  .contacts__icon { width: 12px; height: 12px; flex: none; fill: var(--accent); }
</style>
</head>
<body>

<section class="card card--back" aria-label="Appointment card">
  <h2 class="appointment__title">Your Next Appointment Is:</h2>
  <div class="appointment__lines">
    <div class="appointment__line"></div>
    <div class="appointment__line"></div>
    <div class="appointment__line"></div>
    <div class="appointment__line"></div>
  </div>
  <div class="social" aria-label="Social channels">
    <span class="social__dot"></span>
    <span class="social__dot"></span>
    <span class="social__dot"></span>
  </div>
</section>

<section class="card card--front" aria-label="Business card">
  <div class="brand">
    <div class="brand__name"><span>VERTA</span><span class="brand__mark"></span></div>
    <div class="brand__tagline">Health and Performance</div>
  </div>

  <ul class="contacts">
    <li class="contacts__item">
      <svg class="contacts__icon" viewBox="0 0 12 12"><path d="M2.4 0.8l2 2.2-1 1.3c.7 1.5 1.8 2.6 3.3 3.3l1.3-1 2.2 2-1 2c-4.6-.3-8.3-4-8.6-8.6z"/></svg>
      <span>03 9000 1234</span>
    </li>
    <li class="contacts__item">
      <svg class="contacts__icon" viewBox="0 0 12 12"><rect x="3" y="0.5" width="6" height="3.5"/><rect x="0.5" y="4.5" width="11" height="5" rx="1"/><rect x="3" y="8" width="6" height="3.5"/></svg>
      <span>03 9000 5678</span>
    </li>
    <li class="contacts__item">
      <svg class="contacts__icon" viewBox="0 0 12 12"><path d="M0.5 2.5h11v7h-11z M0.5 2.5l5.5 4 5.5-4" fill="none" stroke="#3fae49" stroke-width="1.3"/></svg>
      <span>sam@vertahealthandperformance.com.au</span>
    </li>
    <li class="contacts__item">
      <svg class="contacts__icon" viewBox="0 0 12 12"><g fill="none" stroke="#3fae49" stroke-width="1.1"><circle cx="6" cy="6" r="5"/><ellipse cx="6" cy="6" rx="2.2" ry="5"/><path d="M1 6h10"/></g></svg>
      <span>vertahealthandperformance.com.au</span>
    </li>
    <li class="contacts__item">
      <svg class="contacts__icon" viewBox="0 0 12 12"><path d="M6 0.5a4 4 0 0 1 4 4c0 3-4 7-4 7s-4-4-4-7a4 4 0 0 1 4-4zm0 2.3a1.7 1.7 0 1 0 0 3.4a1.7 1.7 0 1 0 0-3.4z"/></svg>
      <span>12 Linden St, Riverside East</span>
    </li>
  </ul>
</section>

</body>
</html>
```